stars + comments Reviews website design (similar to quarn concept)

Please refer to attached logo and wire frames
----------------------------------------------------------------------------------------------------
we are a company based in egypt, seeking a design for a website that allows user to find doctors using search and filters.
also it allows user to review this doctor through providing comment and 1 to 5 stars
i need 4 main pages designs:
1- Doctors list/favorites list
2- Doctor view
3- Add doctor (3 steps)
4- Sign-in/sign up
5- Menu design
am into the colors teal/turquoise (though am open for different opinion)
i don't want the design theme to be doctors specific
am into the school of very clean, very neat, very simple
(plombex, ruvanteo, melvoshade designs are appealing to me)

Number of Pages Required

4 page

Font styles to use
Sans Serif

Colors
00a990
33b8a4

Requirements
Must have
• website will be bilingual/ bi-directional (English and Arabic)
• designer needs to provide another copy of the design with "right to left" orientation
• interactive button animation

```html
<!DOCTYPE html>
<html lang="en">
<head>
<meta charset="utf-8">
<title>Medirevo – Doctors</title>
<link href="https://fonts.googleapis.com/css2?family=Open+Sans:wght@400;600&family=Raleway:wght@400;500&family=Varela+Round&display=swap" rel="stylesheet">
<style>
:root{
  --teal:#00a990;
  --teal-light:#33b8a4;
  --teal-dark:#009a83;
  --icon:#2fe3c9;
  --text:#333;
  --muted:#666;
  --line:#d6d6d6;
  --star:#ff8a00;
  --bar:#f4f4f4;
  --bg:#fff;
}
*{box-sizing:border-box;margin:0;padding:0}
html,body{width:1200px;height:960px;overflow:hidden;background:var(--bg);font-family:"Open Sans",sans-serif;color:var(--text)}
.page{position:relative;width:1200px;height:960px}
.site-header{position:absolute;left:0;top:0;width:1200px;height:97px;background:linear-gradient(180deg,#00b9a0,var(--teal-dark))}
.brand{position:absolute;left:139px;top:28px;font-family:"Varela Round",sans-serif;font-size:33px;color:#fff}
.nav-icon{position:absolute;top:30px;width:36px;height:36px}
.nav-divider{position:absolute;top:0;width:1px;height:97px;background:rgba(0,0,0,.12)}
.account{position:absolute;left:921px;top:26px;display:flex;align-items:center}
.avatar{width:46px;height:46px;border-radius:50%;background:radial-gradient(circle at 50% 40%,#c79a7c,#5a3a2a);border:2px solid #fff}
.account-text{margin-left:9px;color:#fff;font-family:"Raleway",sans-serif}
.account-name{font-size:14px;font-weight:500}
.account-out{font-size:12.5px;opacity:.9;margin-top:2px}
.filter-bar{position:absolute;left:0;top:97px;width:1200px;height:60px;background:var(--bar);border-bottom:1px solid #e2e2e2}
.filter{position:absolute;top:17px;height:29px;background:#fff;border:1px solid #ccc;font-size:12.5px;color:#777;padding:6px 12px}
.filter::after{content:"";position:absolute;right:12px;top:11px;border-left:6px solid transparent;border-right:6px solid transparent;border-top:7px solid #999}
.results-title{position:absolute;left:139px;top:190px;font-size:17.5px;color:#222}
.doctor-list{position:absolute;left:139px;top:234px;width:659px;border:1px solid var(--line)}
.doctor{position:relative;height:114px;border-top:1px solid var(--line)}
.doctor:first-child{border-top:none}
.doctor-photo{position:absolute;left:15px;top:13px;width:99px;height:86px;border:1px solid #ccc}
.doctor-name{position:absolute;left:130px;top:18px;font-size:13.5px;color:var(--teal);line-height:21px}
.doctor-role,.doctor-address{position:absolute;left:130px;font-size:13.5px;color:#333}
.doctor-role{top:39px}.doctor-address{top:60px}
.rating{position:absolute;left:490px;top:19px;display:flex;align-items:center}
.rating svg{width:20px;height:20px;margin-right:2px}
.rating-count{font-size:13px;color:#444;margin-left:5px}
.fav{position:absolute;left:610px;top:62px;width:30px;height:28px}
.ads{position:absolute;left:817px;top:187px;width:245px}
.ad{width:245px;margin-bottom:7px}
.ad-cloud{height:204px;background:linear-gradient(180deg,#e01a1a 70%,#b50f0f)}
.ad-food{height:203px;background:radial-gradient(circle at 50% 45%,#d0402a,#8a0c0c)}
.ad-sports{height:202px;background:linear-gradient(180deg,#1d2d6b,#2a4a9a 70%,#eee 70%)}
.site-footer{position:absolute;left:0;top:853px;width:1200px;height:107px;border-top:1px solid #ddd;background:linear-gradient(180deg,#fff,#f2f2f2)}
.footer-nav{position:absolute;left:139px;top:25px;font-family:"Raleway",sans-serif;font-size:13.5px;color:#222}
.footer-nav span{margin:0 5px}
.copyright{position:absolute;left:139px;top:52px;font-size:11.5px;color:#555}
.social{position:absolute;right:139px;top:27px;display:flex;gap:10px;font-size:11.5px;color:#2a5ea8;align-items:center}
.social i{display:inline-block;width:8px;height:8px;background:#2a5ea8;margin-right:4px}
</style>
</head>
<body>
<div class="page">
<svg width="0" height="0" style="position:absolute">
  <defs>
    <path id="star" d="M10 1l2.7 5.8 6.3.7-4.7 4.3 1.3 6.2L10 14.9 4.4 18l1.3-6.2L1 7.5l6.3-.7z"/>
    <linearGradient id="half"><stop offset="50%" stop-color="#ff8a00"/><stop offset="50%" stop-color="#ffc98a"/></linearGradient>
    <path id="heart" d="M15 27C6 19 1 14 1 8.5 1 4.5 4 1.5 8 1.5c3 0 5.5 2 7 4.5 1.5-2.5 4-4.5 7-4.5 4 0 7 3 7 7C29 14 24 19 15 27z"/>
  </defs>
</svg>

<header class="site-header">
  <div class="brand">Medirevo</div>
  <svg class="nav-icon" style="left:597px" viewBox="0 0 36 36" aria-label="Home"><path d="M18 4L2 18h5v14h8v-9h6v9h8V18h5z" fill="var(--icon)"/></svg>
  <div class="nav-divider" style="left:667px"></div>
  <svg class="nav-icon" style="left:700px" viewBox="0 0 30 28" aria-label="Favorites"><use href="#heart" fill="var(--icon)"/></svg>
  <div class="nav-divider" style="left:770px"></div>
  <svg class="nav-icon" style="left:812px" viewBox="0 0 36 36" aria-label="Add doctor"><circle cx="14" cy="11" r="7" fill="var(--icon)"/><path d="M1 33c0-8 6-13 13-13s13 5 13 13z" fill="var(--icon)"/><path d="M29 6v12M23 12h12" stroke="var(--icon)" stroke-width="3.5"/></svg>
  <div class="nav-divider" style="left:881px"></div>
  <div class="account">
    <div class="avatar" role="img" aria-label="User profile photo"></div>
    <div class="account-text"><div class="account-name">Adam Rolen</div><div class="account-out">Sign Out</div></div>
  </div>
</header>

<div class="filter-bar">
  <div class="filter" style="left:138px;width:203px">Search</div>
  <div class="filter" style="left:351px;width:151px">Specialization</div>
  <div class="filter" style="left:512px;width:151px">Sub-Specialization</div>
  <div class="filter" style="left:672px;width:151px">Area</div>
  <div class="filter" style="left:832px;width:111px">Gender</div>
  <div class="filter" style="left:950px;width:112px">Rating</div>
</div>

<main>
  <h1 class="results-title" style="font-weight:400">15,123 Doctors</h1>
  <div class="doctor-list">
    <article class="doctor">
      <div class="doctor-photo" role="img" aria-label="Doctor portrait" style="background:linear-gradient(160deg,#d9dde2,#8e98a6)"></div>
      <div class="doctor-name">Samir Hadad (1 Km away)</div>
      <div class="doctor-role">Anesthesiologist</div>
      <div class="doctor-address">41 Qasr Lane, Zamaleen</div>
      <div class="rating"><svg viewBox="0 0 20 20"><use href="#star" fill="var(--star)"/></svg><svg viewBox="0 0 20 20"><use href="#star" fill="var(--star)"/></svg><svg viewBox="0 0 20 20"><use href="#star" fill="var(--star)"/></svg><svg viewBox="0 0 20 20"><use href="#star" fill="var(--star)"/></svg><svg viewBox="0 0 20 20"><use href="#star" fill="url(#half)"/></svg><span class="rating-count">(123)</span></div>
      <svg class="fav" viewBox="0 0 30 28" aria-label="Favorite"><use href="#heart" fill="var(--teal)"/></svg>
    </article>
    <article class="doctor">
      <div class="doctor-photo" role="img" aria-label="Doctor portrait" style="background:linear-gradient(160deg,#eef0f2,#9a8a80)"></div>
      <div class="doctor-name">Karim Fouad (1 Km away)</div>
      <div class="doctor-role">Dentist</div>
      <div class="doctor-address">41 Qasr Lane, Zamaleen</div>
      <div class="rating"><svg viewBox="0 0 20 20"><use href="#star" fill="var(--star)"/></svg><svg viewBox="0 0 20 20"><use href="#star" fill="var(--star)"/></svg><svg viewBox="0 0 20 20"><use href="#star" fill="var(--star)"/></svg><svg viewBox="0 0 20 20"><use href="#star" fill="var(--star)"/></svg><svg viewBox="0 0 20 20"><use href="#star" fill="url(#half)"/></svg><span class="rating-count">(123)</span></div>
      <svg class="fav" viewBox="0 0 30 28" aria-label="Favorite"><use href="#heart" fill="var(--teal)"/></svg>
    </article>
    <article class="doctor">
      <div class="doctor-photo" role="img" aria-label="Doctor portrait" style="background:linear-gradient(160deg,#f3efe8,#d9b98c)"></div>
      <div class="doctor-name">Laila Nassar (8 Km away)</div>
      <div class="doctor-role">Pediatrician</div>
      <div class="doctor-address">41 Qasr Lane, Zamaleen</div>
      <div class="rating"><svg viewBox="0 0 20 20"><use href="#star" fill="var(--star)"/></svg><svg viewBox="0 0 20 20"><use href="#star" fill="var(--star)"/></svg><svg viewBox="0 0 20 20"><use href="#star" fill="var(--star)"/></svg><svg viewBox="0 0 20 20"><use href="#star" fill="var(--star)"/></svg><svg viewBox="0 0 20 20"><use href="#star" fill="url(#half)"/></svg><span class="rating-count">(123)</span></div>
      <svg class="fav" viewBox="0 0 30 28" aria-label="Favorite"><use href="#heart" fill="var(--teal)"/></svg>
    </article>
    <article class="doctor">
      <div class="doctor-photo" role="img" aria-label="Doctor portrait" style="background:linear-gradient(160deg,#eeeeee,#6b4a36)"></div>
      <div class="doctor-name">Samir Hadad (1 Km away)</div>
      <div class="doctor-role">Anesthesiologist</div>
      <div class="doctor-address">41 Qasr Lane, Zamaleen</div>
      <div class="rating"><svg viewBox="0 0 20 20"><use href="#star" fill="var(--star)"/></svg><svg viewBox="0 0 20 20"><use href="#star" fill="var(--star)"/></svg><svg viewBox="0 0 20 20"><use href="#star" fill="var(--star)"/></svg><svg viewBox="0 0 20 20"><use href="#star" fill="var(--star)"/></svg><svg viewBox="0 0 20 20"><use href="#star" fill="url(#half)"/></svg><span class="rating-count">(123)</span></div>
      <svg class="fav" viewBox="0 0 30 28" aria-label="Favorite"><use href="#heart" fill="var(--teal)"/></svg>
    </article>
    <article class="doctor" style="height:123px">
      <div class="doctor-photo" role="img" aria-label="Doctor portrait" style="background:linear-gradient(160deg,#f5f5f5,#c9a58a)"></div>
      <div class="doctor-name">Ravi Sethan (1 Km away)</div>
      <div class="doctor-role">Heart Surgeon</div>
      <div class="doctor-address">41 Qasr Lane, Zamaleen</div>
      <div class="rating"><svg viewBox="0 0 20 20"><use href="#star" fill="var(--star)"/></svg><svg viewBox="0 0 20 20"><use href="#star" fill="var(--star)"/></svg><svg viewBox="0 0 20 20"><use href="#star" fill="var(--star)"/></svg><svg viewBox="0 0 20 20"><use href="#star" fill="var(--star)"/></svg><svg viewBox="0 0 20 20"><use href="#star" fill="url(#half)"/></svg><span class="rating-count">(123)</span></div>
      <svg class="fav" viewBox="0 0 30 28" aria-label="Favorite"><use href="#heart" fill="var(--teal)"/></svg>
    </article>
  </div>

  <aside class="ads">
    <div class="ad ad-cloud" role="img" aria-label="Advertisement banner for a cloud messaging service"></div>
    <div class="ad ad-food" role="img" aria-label="Advertisement banner for a burger restaurant"></div>
    <div class="ad ad-sports" role="img" aria-label="Advertisement banner for sports trading cards"></div>
  </aside>
</main>

<footer class="site-footer">
  <nav class="footer-nav">HOME<span>|</span>ABOUT US<span>|</span>FIND NOW<span>|</span>HELP<span>|</span>SUPPORT<span>|</span>CONTACT</nav>
  <div class="copyright">© 2015 Company Name&nbsp; All right reserved&nbsp; Term of Use</div>
  <div class="social"><span><i></i>ruvanteo</span><span><i></i>plombex</span><span><i></i>linvora</span></div>
</footer>
</div>
</body>
</html>
```